ROB & JO’S GOODBYE TO MIDGE BITES

I require an attractive appealing label with the dimensions 7.5m x 3.5cm
This is a Natural sandfly insect repellent cream formulated by 2 pharmacists Carla Whitby and Rob Kettering. It is required for labelling a 50 g jar

Contains Essential Oils of cedar wood, rosemary, cinnamon, citronella, lavender, eucalyptus and clove in a moisturising base.

We would like to see designs using the colour bright duck egg blue as the main colour with dark brown tones for the patterns. An eye catching label is output aim . However any colour combination that is attractive to the eye is welcome
A gloss finish is preferable.

More designs please

Target Market(s)

Trekkers, outdoor active people, pharmacy, health shops

Colors
abd037
34a6d7
0456a4
33b8a4

Requirements
Must have
• Rob and Jo’s
• Goodbye to Midge bites
• Natural Sandfly Repellent
• Contains Essential Oils of cedar wood, rosemary, cinnamon, citronella, lavender, eucalyptus and clove in a moisturising base.
• Formulated by Australian Pharmacists Carla Whitby and Rob Kettering
• Made in Australia
• 0413862207
Nice to have
• Sandfly/ flies
• I have attached a label I use for my mozzie cream and would like a similar font please

```html
<!DOCTYPE html>
<html lang="en">
<head>
<meta charset="utf-8">
<title>Rob and Jo’s Repellent Labels</title>
<link rel="stylesheet" href="https://fonts.googleapis.com/css2?family=Josefin+Sans:wght@400;600&family=Yellowtail&display=swap">
<style>
  :root{
    --page:#ffffff;
    --sky:#8fd3ef;
    --mint:#a5d5a6;
    --brown:#6e5248;
    --white:#ffffff;
    --sun:#fbd955;
    --coral:#e2644b;
    --cyan:#27b8dd;
    --lilac:#8582b6;
  }
  *{margin:0;padding:0;box-sizing:border-box}
  html,body{width:1200px;height:1200px;overflow:hidden;background:var(--page)}
  .label{position:absolute;overflow:hidden}
  .label--sandfly{left:68px;top:84px;width:1052px;height:490px}
  .label--mozzie{left:64px;top:641px;width:1048px;height:488px}
  .pattern{position:absolute;inset:0}
  .label--sandfly .pattern{background:var(--sky)}
  .label--mozzie .pattern{background:var(--mint)}
  .script{
    position:absolute;width:300px;text-align:center;
    font-family:"Yellowtail",cursive;font-size:64px;line-height:68px;color:var(--brown);
    text-shadow:2px 0 0 var(--white),-2px 0 0 var(--white),0 2px 0 var(--white),0 -2px 0 var(--white),
      2px 2px 0 var(--white),-2px -2px 0 var(--white),2px -2px 0 var(--white),-2px 2px 0 var(--white),4px 5px 4px rgba(0,0,0,.35);
  }
  .script--left{left:0;top:55px}
  .script--right{left:748px;top:50px}
  .brand{
    position:absolute;width:216px;height:216px;border-radius:50%;background:var(--white);
    display:flex;align-items:center;justify-content:center;text-align:center;
    font-family:"Josefin Sans",sans-serif;font-weight:600;font-size:30px;line-height:36px;color:var(--brown);
  }
  .label--sandfly .brand{left:422px;top:53px}
  .label--mozzie .brand{left:422px;top:53px}
  .tagline{
    position:absolute;left:0;right:0;text-align:center;
    font-family:"Josefin Sans",sans-serif;font-weight:400;font-size:40px;letter-spacing:1px;color:var(--white);
    text-shadow:1.5px 0 0 var(--brown),-1.5px 0 0 var(--brown),0 1.5px 0 var(--brown),0 -1.5px 0 var(--brown);
  }
  .label--sandfly .tagline{top:272px}
  .label--mozzie .tagline{top:272px}
  .band{
    position:absolute;left:8px;right:8px;height:64px;
    display:flex;flex-direction:column;justify-content:center;align-items:center;text-align:center;
    font-family:"Josefin Sans",sans-serif;font-weight:400;font-size:17px;line-height:25px;color:var(--white);
  }
  .band--ingredients{top:325px}
  .band--credits{top:404px}
  .label--mozzie .band{left:7px;right:7px}
  .label--mozzie .band--credits{top:402px}
  .band--ingredients .outlined{
    text-shadow:1px 0 0 var(--brown),-1px 0 0 var(--brown),0 1px 0 var(--brown),0 -1px 0 var(--brown);
  }
  .label--sandfly .band--ingredients{background:var(--sun)}
  .label--sandfly .band--credits{background:var(--coral)}
  .label--mozzie .band--ingredients{background:var(--cyan)}
  .label--mozzie .band--credits{background:var(--lilac)}
</style>
</head>
<body>

<section class="label label--sandfly">
  <div class="pattern" role="img" aria-label="Repeating pattern of small brown sandfly drawings on duck egg blue"></div>
  <p class="script script--left">Natural<br>Sandfly<br>Repellent</p>
  <p class="script script--right">Natural<br>Sandfly<br>Repellent</p>
  <div class="brand">ROB AND<br>JO’S</div>
  <h1 class="tagline">GOODBYE TO MIDGE BITES</h1>
  <div class="band band--ingredients"><span class="outlined">CONTAINS ESSENTIAL OILS OF CEDAR WOOD, ROSEMARY, CINNAMON, CITRONELLA, LAVENDER,</span><span class="outlined">EUCALYPTUS AND CLOVE IN A MOISTURISING BASE.</span></div>
  <div class="band band--credits"><span>FORMULATED BY AUSTRALIAN PHARMACISTS CARLA WHITBY AND ROB KETTERING</span><span>MADE IN AUSTRALIA – 0413862207</span></div>
</section>

<section class="label label--mozzie">
  <div class="pattern" role="img" aria-label="Repeating pattern of small brown mosquito drawings on soft green"></div>
  <p class="script script--left">Natural<br>Mozzie<br>Repellent</p>
  <p class="script script--right">Natural<br>Mozzie<br>Repellent</p>
  <div class="brand">ROB AND<br>JO’S</div>
  <h2 class="tagline">GOODBYE TO MOZZIE BITES</h2>
  <div class="band band--ingredients"><span>CONTAINS ESSENTIAL OILS OF CEDAR WOOD, ROSEMARY, CINNAMON AND CITRONELLA IN A</span><span>SPECIAL OLIVE OIL BASE.</span></div>
  <div class="band band--credits"><span>FORMULATED BY AUSTRALIAN PHARMACISTS CARLA WHITBY AND ROB KETTERING</span><span>MADE IN AUSTRALIA – 0413862207</span></div>
</section>

</body>
</html>
```